High-end Oceanfront Real Estate Group Needs Clean, Modern Web Design

I’m looking for a clean, professional, modern and beautiful homepage web design for a Real Estate group in Southern California, USA.

The group/company is “Marlow on the Shore,” and they specialize in high end (i.e. expensive), oceanfront real estate in the Orange County area.

The look and feel of the page should accentuate the brand qualities: luxurious/expensive, professional, and beautiful (Orange County is one of the most beautiful areas in all the US and we would love the site to emphasize the beautiful beaches and scenery it has to offer).

Looks we like:
• www.brantleyhomesrealty.example
• www.keptbyfenwick.example -- I think the design is pretty out-dated in this site, but I like the organization/layout of the site

Header Tags (I don’t know if we can fit all of these, may need a side-menu, but I’d prefer header title only if possible):
• Welcome
• Featured Listings
• Previously Sold
• Sell
• Property Search
• Team
• Videos
• Blog
• Explore O.C.
• Contact

I have attached the beach and logo pics that we would like to use as the header, a few pictures of the team, and one sample home/view pic which can be used in any of the other sections (for pictures of the homes, just find expensive oceanfront houses and that will be fine).

I promise to provide feedback to each and every design submission. I appreciate the hard work that all of you are putting into your designs. There can be only one contest winner, but I hope to give all of you helpful feedback to submit the best designs possible!

Target Market(s)

Very wealthy home owners of oceanfront properties. These properties are worth several millions of dollars, and thus the site and brand needs to be targeted to very wealthy, successful individuals and families (both US and international buyers).

Industry/Entity Type

Real Estate

Number of Pages Required

2 page

Requirements
Must have
• I don’t want to give too many requirements, because I want to let you all be creative. However, here are the few Must Haves:
• Must submit 2 page designs (a home page and a sub page)
• Must use logo provided
• Focus is mostly on homes, but I would like to include some beach/ocean imagery as well
• The first “item” on the home page should be an accordion/slider which shows pictures of homes and with 1 line of text: “List with the Leader” and two link buttons: “Sell Your Home” and “Buy Your Home”
• Color palette needs to be mainly blues--to match ocean and sky blue
• Exported in all major formats (psd,ai,eps,png,jpeg,etc)
Nice to have
• We don’t necessarily need all of these, but would like to feature most:
• List of videos
• “Meet the Team”—brief team bios and pics
• Link(s) to Blog
• “List with the Leader” – section on why they should choose this firm
• Featured Listings
• Previously Sold

```html
<!DOCTYPE html>
<html lang="en">
<head>
<meta charset="utf-8">
<title>Marlow on the Shore — Oceanfront Real Estate</title>
<link href="https://fonts.googleapis.com/css2?family=Raleway:wght@300;400;600;700&family=Open+Sans:ital,wght@0,400;0,600;0,700;1,400&display=swap" rel="stylesheet">
<style>
:root{
  --blue:#1f63a6;
  --blue-dark:#174e85;
  --ink:#333;
  --muted:#777;
  --line:#dcdcdc;
  --pale:#f2f2f2;
  --dark:#3c3c3c;
  --darker:#2b2b2b;
  --white:#fff;
}
*{box-sizing:border-box;margin:0;padding:0}
html,body{width:1200px;height:4009px;overflow:hidden}
body{font-family:"Open Sans",Arial,sans-serif;color:var(--ink);background:var(--white);position:relative}
section,header,footer{position:absolute;left:0;width:1200px}
.abs{position:absolute}
.h-title{font-family:"Raleway",Arial,sans-serif;font-weight:400;font-size:32px;letter-spacing:1px;text-align:center;color:#333;text-transform:uppercase}
.h-title b{color:var(--blue);font-weight:600}
.lede{font-size:14px;line-height:26px;color:var(--muted);text-align:center;width:940px;left:130px}
.btn{display:inline-flex;align-items:center;justify-content:center;font-family:"Open Sans",sans-serif;font-weight:600;font-size:15px;color:var(--white);background:var(--blue)}

/* hero slider */
.hero{top:0;height:695px;background:linear-gradient(180deg,#9fb5c6 0%,#c9d7df 30%,#7ea7c3 55%,#2f6e9c 72%,#6b6b6f 82%,#3a3a3e 100%)}
.hero-shade{left:0;top:250px;width:640px;height:200px;background:linear-gradient(90deg,rgba(0,0,0,.35),rgba(0,0,0,0))}
.brand{left:94px;top:0;width:219px;height:152px;background:rgba(255,255,255,.9);border:1px solid #b8c9d8;display:flex;align-items:center;justify-content:center;gap:10px}
.brand-dot{width:18px;height:18px;border-radius:50%;background:var(--blue)}
.brand-name{font-family:"Raleway",sans-serif;font-weight:600;font-size:25px;line-height:30px;color:var(--blue);text-transform:uppercase;width:140px}
.topbar{left:313px;top:0;width:797px;height:102px;background:rgba(255,255,255,.92);display:flex}
.topbar .info{flex:1;padding-top:26px;display:flex;flex-direction:column;align-items:center;border-right:1px solid #e2e2e2}
.topbar .info:last-child{border-right:0}
.info small{display:flex;align-items:center;gap:8px;font-size:12px;color:#8a8a8a}
.info small svg{width:14px;height:14px}
.info strong{display:block;font-size:17px;font-weight:600;color:#333;margin-top:6px;white-space:nowrap}
.nav{left:313px;top:102px;width:797px;height:50px;background:var(--blue);display:flex;justify-content:flex-end;align-items:stretch;padding-right:10px}
.nav a{color:var(--white);text-decoration:none;font-size:13px;font-weight:600;padding:0 13px;display:flex;align-items:center;text-transform:uppercase}
.nav a.active{background:#2d3a45}
.hero-copy{left:107px;top:262px;color:var(--white)}
.hero-copy .tag{font-size:15px;font-weight:700;letter-spacing:3px;text-transform:uppercase;margin-bottom:6px}
.hero-copy .l1{font-family:"Raleway",sans-serif;font-weight:300;font-size:50px;line-height:58px}
.hero-copy .l2{font-family:"Raleway",sans-serif;font-weight:400;font-size:50px;line-height:62px;text-transform:uppercase}
.hero-copy .l2 b{font-weight:700}
.hero-copy .l2 span{text-transform:none}
.hero-copy .l3{font-size:17px;font-weight:700;margin-top:4px}
.dots{left:0;width:1200px;top:660px;display:flex;justify-content:center;gap:10px}
.dots span{width:10px;height:10px;border-radius:50%;background:rgba(255,255,255,.5)}
.dots span.on{background:var(--white)}

/* quote */
.quote{top:695px;height:134px;background:var(--dark)}
.quote h3{left:110px;top:44px;color:var(--white);font-size:19px;font-weight:700;line-height:22px;text-transform:uppercase}
.field{top:30px;width:178px}
.field label{display:block;color:var(--white);font-size:13px;font-weight:600;margin-bottom:8px}
.field div{height:44px;background:var(--white)}
.quote .btn{left:947px;top:56px;width:143px;height:44px}

/* welcome */
.welcome{top:829px;height:668px}
.feature{width:260px;text-align:center}
.feature .ico{width:86px;height:86px;border-radius:50%;background:var(--blue);margin:0 auto;display:flex;align-items:center;justify-content:center}
.feature h4{font-size:17px;font-weight:400;margin-top:22px;text-transform:uppercase;letter-spacing:.5px}
.feature p{font-size:13px;font-style:italic;color:#888;line-height:22px;margin-top:14px;padding:0 20px}
.btn-outline{background:var(--white);color:#333;border:1px solid #555}

/* about */
.about{top:1497px;height:494px;background:var(--pale)}
.about h2{left:110px;top:95px;font-family:"Raleway",sans-serif;font-weight:400;font-size:32px;line-height:44px;text-transform:uppercase}
.about h2 b{color:var(--blue);font-weight:400}
.about p{left:110px;top:200px;width:440px;font-size:13px;line-height:24px;color:#555}
.about .btn{left:110px;top:353px;width:183px;height:52px}
.video{left:633px;top:86px;width:457px;height:320px;background:linear-gradient(135deg,#8d8d8d,#d4d4d4 45%,#5e5e5e)}
.video-bar{left:0;bottom:0;width:457px;height:50px;background:#1a1a1a}
.play{left:200px;top:118px;width:56px;height:44px;background:rgba(0,0,0,.75);border-radius:8px;display:flex;align-items:center;justify-content:center}

/* listings */
.listings{top:1991px;height:615px;background:var(--white)}
.listings-cap{left:107px;top:0;width:983px;height:80px;background:var(--white)}
.listings-bg{left:0;top:0;width:1200px;height:80px;background:var(--pale)}
.card{top:201px;width:291px}
.card .photo{height:208px}
.card h5{position:absolute;top:240px;left:0;font-size:15px;font-weight:600;text-transform:uppercase}
.card .price{position:absolute;top:240px;right:0;font-size:16px;font-weight:700;color:var(--blue)}
.card .sub{position:absolute;top:274px;left:0;font-size:13px;color:#777;white-space:nowrap}
.card .meta{position:absolute;top:312px;left:0;font-size:13px;color:#555;display:flex;gap:18px}
.card .meta span{display:flex;align-items:center;gap:6px}
.card .btn{position:absolute;top:302px;right:0;width:104px;height:38px;font-size:13px}
.sold{position:absolute;left:16px;top:18px;width:60px;height:24px;border:1px solid #2d6da8;color:#2d6da8;background:rgba(255,255,255,.8);font-size:12px;display:flex;align-items:center;justify-content:center}
.arrow{width:44px;height:44px;border-radius:50%;border:2px solid #9a9a9a;display:flex;align-items:center;justify-content:center;background:var(--white)}

/* team */
.team{top:2606px;height:602px;background:var(--pale)}
.portrait{left:187px;top:187px;width:267px;height:415px;background:linear-gradient(180deg,#e6e2dd,#c9a98d 55%,#e8d8c8)}
.team h3{left:590px;top:250px;font-family:"Raleway",sans-serif;font-weight:400;font-size:40px;color:var(--blue)}
.team .bio{left:590px;top:326px;width:500px;font-size:13px;line-height:26px;color:#555}
.team .contact{left:590px;top:440px;font-size:13px;line-height:34px;color:#555}
.socials{left:590px;top:517px;display:flex;gap:6px}
.socials span{width:30px;height:30px;border-radius:50%;background:var(--blue)}

/* testimonials */
.testimonials{top:3208px;height:534px}
.quote-card{top:232px;width:423px;height:128px;background:var(--white);box-shadow:0 0 0 1px #e8e8e8,0 4px 10px rgba(0,0,0,.08);padding:22px 30px 0 72px;font-size:13px;line-height:21px;color:#555}
.quote-card .mark{position:absolute;left:22px;top:10px;font-family:Georgia,serif;font-size:60px;color:#ccc;line-height:60px}
.quote-card .tail{position:absolute;left:36px;bottom:-12px;width:22px;height:22px;background:var(--white);transform:rotate(45deg);box-shadow:2px 2px 0 0 #e8e8e8}
.author{top:386px;display:flex;align-items:center;gap:16px}
.author .face{width:74px;height:74px;border-radius:50%;background:linear-gradient(180deg,#d9d9d9,#a8a8a8);border:3px solid #fff;box-shadow:0 0 0 1px #ddd}
.author b{display:block;font-size:16px;font-weight:600;color:#e07a2f}
.author small{font-size:13px;color:#777}

/* footer */
.site-footer{top:3742px;height:214px;background:var(--dark);color:#cfcfcf}
.fcol{top:44px}
.fcol h6{font-size:14px;font-weight:600;color:var(--white);text-transform:uppercase;padding-bottom:8px;border-bottom:1px solid #666;width:120px;margin-bottom:10px}
.fcol li{list-style:none;font-size:12px;line-height:24px}
.faddr{left:847px;top:44px;font-size:12px;line-height:24px}
.fsoc{left:847px;top:152px;display:flex;gap:8px}
.fsoc span{width:30px;height:30px;border-radius:50%;background:var(--white)}
.bottom-bar{top:3956px;height:53px;background:var(--darker);color:#ddd;font-size:12px}
</style>
</head>
<body>

<header class="hero" role="img" aria-label="Slider of oceanfront homes: bright bedroom with wide windows overlooking the blue sea and a passing yacht">
  <div class="abs hero-shade"></div>
  <div class="abs brand"><span class="brand-dot"></span><span class="brand-name">Marlow on the Shore</span></div>
  <div class="abs topbar">
    <div class="info">
      <small><svg viewBox="0 0 16 16"><path d="M3 1h3l1 4-2 1a9 9 0 0 0 5 5l1-2 4 1v3c0 1-1 2-2 2A13 13 0 0 1 1 3c0-1 1-2 2-2z" fill="#5b8fc4"/></svg>Free Call For You</small>
      <strong>949 555 01427</strong>
    </div>
    <div class="info">
      <small><svg viewBox="0 0 16 16"><rect x="1" y="3" width="14" height="10" rx="1" fill="none" stroke="#5b8fc4" stroke-width="1.6"/><path d="M1 4l7 5 7-5" fill="none" stroke="#5b8fc4" stroke-width="1.6"/></svg>Email Us</small>
      <strong>mail@marlowshore.example</strong>
    </div>
    <div class="info">
      <small><svg viewBox="0 0 16 16"><circle cx="8" cy="8" r="6.5" fill="none" stroke="#5b8fc4" stroke-width="1.6"/><path d="M8 4v4l3 2" fill="none" stroke="#5b8fc4" stroke-width="1.6"/></svg>Opening Hours</small>
      <strong>08:00 - 14:00</strong>
    </div>
  </div>
  <nav class="abs nav">
    <a class="active" href="#">Home</a><a href="#">Featured Listings</a><a href="#">Sold</a><a href="#">Sell</a><a href="#">Team</a><a href="#">Videos</a><a href="#">Blog</a><a href="#">Contact</a>
  </nav>
  <div class="abs hero-copy">
    <div class="tag">List with the Leader</div>
    <div class="l1">Whether You’re</div>
    <div class="l2"><b>Selling</b> <span>Or</span> <b>Buying</b></div>
    <div class="l3">We Treat Your Most VALUABLE ASSET As If It Were Our Own</div>
  </div>
  <div class="abs dots"><span class="on"></span><span></span><span></span></div>
</header>

<section class="quote">
  <h3 class="abs">Get a<br>Free Quote</h3>
  <div class="abs field" style="left:310px"><label>Full Name</label><div></div></div>
  <div class="abs field" style="left:510px"><label>Email Adress</label><div></div></div>
  <div class="abs field" style="left:708px"><label>Phone Number</label><div></div></div>
  <span class="abs btn">Get a Qoute</span>
</section>

<section class="welcome">
  <h2 class="abs h-title" style="left:0;width:1200px;top:68px">Welcome to <b>Marlow on the Shore</b></h2>
  <p class="abs lede" style="top:128px">Lorem ipsum dolor sit amet, consectetur adipiscing elit, sed do eiusmod tempor incididunt ut labore et dolore magna aliqua. Ut enim ad minim veniam, quis nostrud exercitation ullamco laboris nisi ut aliquip ex ea commodo consequat.</p>
  <div class="abs feature" style="left:90px;top:245px">
    <div class="ico"><svg width="42" height="34" viewBox="0 0 42 34"><path d="M8 20h26l-4 8H12z M14 20l4-10h8l6 10" fill="#fff"/><path d="M2 30c5 0 5 3 10 3s5-3 10-3 5 3 10 3 5-3 8-3" stroke="#fff" stroke-width="2" fill="none"/></svg></div>
    <h4>Best Location</h4>
    <p>Lorem ipsum dolor sit amet, consectetur adipiscing elit. In ac risus ut turpis dignissim congue.</p>
  </div>
  <div class="abs feature" style="left:470px;top:245px">
    <div class="ico"><svg width="40" height="40" viewBox="0 0 40 40"><circle cx="14" cy="10" r="5" fill="#fff"/><circle cx="27" cy="12" r="4" fill="#fff"/><path d="M6 34v-10c0-4 4-7 8-7s8 3 8 7v10z M22 34v-8c0-3 2-6 5-6s6 3 6 6v8z" fill="#fff"/></svg></div>
    <h4>Trusted Agents</h4>
    <p>Lorem ipsum dolor sit amet, consectetur adipiscing elit. In ac risus ut turpis dignissim congue.</p>
  </div>
  <div class="abs feature" style="left:840px;top:245px">
    <div class="ico"><svg width="40" height="40" viewBox="0 0 40 40"><path d="M20 5a15 15 0 1 1-14 10" fill="none" stroke="#fff" stroke-width="3"/><path d="M20 12v9l6 4" fill="none" stroke="#fff" stroke-width="3"/><path d="M2 12l5 4 4-6" fill="none" stroke="#fff" stroke-width="3"/></svg></div>
    <h4>Save Time</h4>
    <p>Lorem ipsum dolor sit amet, consectetur adipiscing elit. In ac risus ut turpis dignissim congue.</p>
  </div>
  <span class="abs btn" style="left:396px;top:558px;width:184px;height:51px">Sell Your Home</span>
  <span class="abs btn btn-outline" style="left:615px;top:558px;width:182px;height:51px">Buy Your Home</span>
</section>

<section class="about">
  <h2 class="abs">Orange County’s Best<br><b>Real Estate Proffessionals</b></h2>
  <p class="abs">We at Marlow on the Shore are privileged to help people from all over the world find their dream homes in Monarch Beach, Laguna Beach, Newport Coast, Dana Point, San Clemente and San Juan Capistrano. Whether you are buying or selling a property in Orange County, we want to help you in the most efficient, professional way possible.</p>
  <span class="abs btn">Contact Us Now</span>
  <div class="abs video" role="img" aria-label="Video still of agents meeting clients around a table">
    <div class="abs play"><svg width="20" height="22" viewBox="0 0 20 22"><path d="M2 1l17 10L2 21z" fill="#fff"/></svg></div>
    <div class="abs video-bar">
      <svg width="457" height="50" viewBox="0 0 457 50"><path d="M12 18l12 7-12 7z" fill="#fff"/><rect x="0" y="0" width="457" height="3" fill="#444"/><rect x="0" y="0" width="260" height="3" fill="#d33"/><text x="40" y="30" fill="#bbb" font-size="9" font-family="Open Sans">00:06 / 01:23</text><rect x="330" y="22" width="60" height="4" fill="#d33"/><rect x="420" y="16" width="14" height="14" fill="none" stroke="#fff" stroke-width="2"/></svg>
    </div>
  </div>
</section>

<section class="listings">
  <div class="abs listings-bg"></div>
  <div class="abs listings-cap"></div>
  <h2 class="abs h-title" style="left:0;width:1200px;top:40px">Featured <b>Listing</b></h2>
  <p class="abs lede" style="top:98px">Lorem ipsum dolor sit amet, consectetur adipiscing elit, sed do eiusmod tempor incididunt ut labore et dolore magna aliqua. Ut enim ad minim veniam, quis nostrud exercitation ullamco laboris nisi ut aliquip ex ea commodo consequat.</p>
  <div class="abs arrow" style="left:35px;top:277px"><svg width="18" height="14" viewBox="0 0 18 14"><path d="M17 7H2M7 1L1 7l6 6" stroke="#888" stroke-width="2" fill="none"/></svg></div>
  <div class="abs arrow" style="left:1120px;top:277px"><svg width="18" height="14" viewBox="0 0 18 14"><path d="M1 7h15M11 1l6 6-6 6" stroke="#888" stroke-width="2" fill="none"/></svg></div>

  <div class="abs card" style="left:110px">
    <div class="photo" role="img" aria-label="Beachfront villa bedroom with glass walls" style="background:linear-gradient(135deg,#cfc6b8,#8a7a66 50%,#e6e1d8)"></div>
    <h5>Beach Front Villa</h5><span class="price">$ 123456</span>
    <span class="sub">Lorem Ipsum Dolor Sit Amet Consectetuer</span>
    <div class="meta"><span><svg width="18" height="12" viewBox="0 0 18 12"><path d="M1 2v9M1 7h16v4M4 7V4h6v3" stroke="#666" stroke-width="1.6" fill="none"/></svg>3 Rooms</span><span><svg width="16" height="14" viewBox="0 0 16 14"><path d="M1 6h14v3a4 4 0 0 1-4 4H5a4 4 0 0 1-4-4z M3 6V2h3" stroke="#666" stroke-width="1.6" fill="none"/></svg>2 Baths</span></div>
    <span class="btn">VIEW MORE</span>
  </div>
  <div class="abs card" style="left:454px">
    <div class="photo" role="img" aria-label="Bright living room of a sold villa facing the sea" style="background:linear-gradient(135deg,#e8eef2,#aebfcc 50%,#f1f1ef);position:relative"><span class="sold">SOLD</span></div>
    <h5>Beach Front Villa</h5><span class="price">$ 123456</span>
    <span class="sub">Lorem Ipsum Dolor Sit Amet Consectetuer</span>
    <div class="meta"><span><svg width="18" height="12" viewBox="0 0 18 12"><path d="M1 2v9M1 7h16v4M4 7V4h6v3" stroke="#666" stroke-width="1.6" fill="none"/></svg>3 Rooms</span><span><svg width="16" height="14" viewBox="0 0 16 14"><path d="M1 6h14v3a4 4 0 0 1-4 4H5a4 4 0 0 1-4-4z M3 6V2h3" stroke="#666" stroke-width="1.6" fill="none"/></svg>2 Baths</span></div>
    <span class="btn">VIEW MORE</span>
  </div>
  <div class="abs card" style="left:799px">
    <div class="photo" role="img" aria-label="Modern villa exterior lit at dusk" style="background:linear-gradient(180deg,#3a4a63,#7a6a58 60%,#2f3a25)"></div>
    <h5>Beach Front Villa</h5><span class="price">$ 123456</span>
    <span class="sub">Lorem Ipsum Dolor Sit Amet Consectetuer</span>
    <div class="meta"><span><svg width="18" height="12" viewBox="0 0 18 12"><path d="M1 2v9M1 7h16v4M4 7V4h6v3" stroke="#666" stroke-width="1.6" fill="none"/></svg>3 Rooms</span><span><svg width="16" height="14" viewBox="0 0 16 14"><path d="M1 6h14v3a4 4 0 0 1-4 4H5a4 4 0 0 1-4-4z M3 6V2h3" stroke="#666" stroke-width="1.6" fill="none"/></svg>2 Baths</span></div>
    <span class="btn">VIEW MORE</span>
  </div>
</section>

<section class="team">
  <h2 class="abs h-title" style="left:0;width:1200px;top:50px">Meet Our <b>Team</b></h2>
  <p class="abs lede" style="top:110px">Lorem ipsum dolor sit amet, consectetur adipiscing elit, sed do eiusmod tempor incididunt ut labore et dolore magna aliqua. Ut enim ad minim veniam, quis nostrud exercitation ullamco laboris nisi ut aliquip ex ea commodo consequat.</p>
  <div class="abs arrow" style="left:35px;top:345px"><svg width="18" height="14" viewBox="0 0 18 14"><path d="M17 7H2M7 1L1 7l6 6" stroke="#888" stroke-width="2" fill="none"/></svg></div>
  <div class="abs arrow" style="left:1120px;top:345px"><svg width="18" height="14" viewBox="0 0 18 14"><path d="M1 7h15M11 1l6 6-6 6" stroke="#888" stroke-width="2" fill="none"/></svg></div>
  <div class="abs portrait" role="img" aria-label="Portrait of lead agent Elise Marlow in a light blazer"></div>
  <h3 class="abs">Elise Marlow</h3>
  <p class="abs bio">Lorem ipsum dolor sit amet, consectetur adipiscing elit, sed do eiusmod tempor incididunt ut labore et dolore magna aliqua. Ut enim ad minim veniam, quis nostrud exercitation ullamco laboris nisi ut aliquip ex ea commodo consequat.</p>
  <div class="abs contact">mail@marlowshore.example<br>949 555 01427</div>
  <div class="abs socials"><span></span><span></span><span></span></div>
</section>

<section class="testimonials">
  <h2 class="abs h-title" style="left:0;width:1200px;top:50px">Customer <b>Testimonials</b></h2>
  <p class="abs lede" style="top:110px">Lorem ipsum dolor sit amet, consectetur adipiscing elit, sed do eiusmod tempor incididunt ut labore et dolore magna aliqua. Ut enim ad minim veniam, quis nostrud exercitation ullamco laboris nisi ut aliquip ex ea commodo consequat.</p>
  <div class="abs quote-card" style="left:152px"><span class="mark">“</span>Lorem ipsum dolor sit amet, consectetur adipiscing elit. Etiam vulputate, diam vitae cursus aliquet, ante orci euismod augue, id mattis nulla odio eget enim. Etiam lobortis, diam in .<span class="tail"></span></div>
  <div class="abs quote-card" style="left:615px"><span class="mark">“</span>Lorem ipsum dolor sit amet, consectetur adipiscing elit. Etiam vulputate, diam vitae cursus aliquet, ante orci euismod augue, id mattis nulla odio eget enim. Etiam lobortis, diam in .<span class="tail"></span></div>
  <div class="abs author" style="left:160px"><div class="face" role="img" aria-label="Client photo"></div><div><b>Aliquet Nulla</b><small>Harborline Studios, Founder CEO</small></div></div>
  <div class="abs author" style="left:623px"><div class="face" role="img" aria-label="Client photo"></div><div><b>Donec Pellentesque</b><small>Harborline Studios, Founder CEO</small></div></div>
</section>

<footer class="site-footer">
  <div class="abs fcol" style="left:140px"><h6>About Us</h6><ul><li>About Us</li><li>Privacy Policy</li><li>Terms of Use</li><li>Contact Us</li><li>Site Map</li></ul></div>
  <div class="abs fcol" style="left:302px"><h6>Info</h6><ul><li>Retail Malls</li><li>Shopping Complex</li><li>High Street Villas</li><li>Retail Houses</li></ul></div>
  <div class="abs fcol" style="left:472px"><h6>Community</h6><ul><li>Blog</li><li>Support</li><li>Translation Tool</li><li>Developer</li></ul></div>
  <div class="abs fcol" style="left:646px"><h6>Support Us</h6><ul><li>Knowledgebase</li><li>Download &amp; Update</li><li>Information</li><li>Documentation</li></ul></div>
  <div class="abs faddr">Harbor Way 1246<br>Newport Coast CA<br>Phone: +1 949 555 0142<br>Email: info@marlowshore.example</div>
  <div class="abs fsoc"><span></span><span></span><span></span></div>
</footer>
<div class="abs bottom-bar" style="left:0;width:1200px">
  <span class="abs" style="left:112px;top:18px">Copyrights © 2014 Marlow on the Shore - All Rights Reserved</span>
  <span class="abs" style="left:890px;top:18px">Privacy Policy &nbsp; | &nbsp; Terms &amp; Condition</span>
</div>

</body>
</html>
```